New business card for civil engineering company - "Keystone Audit"

We need a business card designed for our new structural engineering company.

The company name is "Keystone Audit" logo files attached.

We would like the following:
* Two-sided card
* Simple design

Information to be placed on the card:
Name - Marcus Dellow
Job Title - Director / Structural Engineer
Credentials - BEng(Hons), CPEng, CMengNZ, IntPE(NZ)
Email - marcus.dellow@keystoneaudit.co.nz
mobile - 0219364058
website - www.keystoneaudit.co.nz

```html
<!DOCTYPE html>
<html lang="en">
<head>
<meta charset="utf-8">
<title>Keystone Audit – Business Card</title>
<link href="https://fonts.googleapis.com/css2?family=Lato:wght@400;700&display=swap" rel="stylesheet">
<style>
  :root {
    --page-bg: #e9ebee;
    --navy: #0b3f6e;
    --brand-blue: #1a78c2;
    --charcoal: #3a3a3a;
    --text-grey: #454545;
    --muted-grey: #9a9a9a;
    --white: #ffffff;
    --divider: #3b8fd0;
  }
  * { box-sizing: border-box; margin: 0; padding: 0; }
  html, body {
    width: 1200px; height: 912px; overflow: hidden;
    background: var(--page-bg);
    font-family: "Lato", sans-serif;
  }
  .sheet {
    width: 1200px; height: 912px;
    display: flex; flex-direction: column; align-items: center; justify-content: center;
    gap: 32px;
  }
  .card {
    position: relative;
    width: 700px; height: 400px;
    border-radius: 22px;
    overflow: hidden;
    box-shadow: 0 6px 18px rgba(0,0,0,0.18);
  }

  /* Back side */
  .card--back {
    background: var(--navy);
    display: flex; align-items: center; justify-content: center;
  }
  .brand {
    display: flex; flex-direction: column; align-items: center; gap: 8px;
  }
  .brand__name {
    font-weight: 700;
    font-size: 38px;
    letter-spacing: 2px;
    text-transform: uppercase;
  }
  .brand__tagline {
    font-size: 12px;
    letter-spacing: 3.5px;
    text-transform: uppercase;
  }
  .card--back .brand__name { color: var(--white); }
  .card--back .brand__tagline { color: #cfe0f0; }

  /* Front side */
  .card--front { background: var(--white); }
  .card--front .brand {
    position: absolute; left: 40px; top: 150px; width: 300px;
  }
  .card--front .brand__name { color: var(--charcoal); font-size: 30px; }
  .card--front .brand__tagline { color: var(--muted-grey); font-size: 10px; letter-spacing: 3px; }

  .divider {
    position: absolute; left: 372px; top: 62px;
    width: 1.5px; height: 190px;
    background: var(--divider);
  }
  .contact {
    position: absolute; left: 400px; top: 58px; right: 20px;
    color: var(--text-grey);
  }
  .contact__name {
    color: var(--brand-blue);
    font-size: 30px; font-weight: 700;
    text-transform: uppercase;
    line-height: 1.05;
    margin-bottom: 6px;
  }
  .contact__role, .contact__creds {
    font-size: 16px; line-height: 1.3;
  }
  .contact__list {
    list-style: none; margin-top: 16px;
    font-size: 16px; line-height: 1.55;
  }
  .contact__list li { display: flex; align-items: center; gap: 8px; }
  .contact__list svg { width: 12px; height: 12px; flex: none; }

  .swoosh {
    position: absolute; left: 0; bottom: 0; width: 700px; height: 400px;
  }
</style>
</head>
<body>
<main class="sheet">

  <section class="card card--back" aria-label="Card back">
    <div class="brand">
      <span class="brand__name">Keystone Audit</span>
      <span class="brand__tagline">Peer Review Specialists</span>
    </div>
  </section>

  <section class="card card--front" aria-label="Card front">
    <svg class="swoosh" viewBox="0 0 700 400" preserveAspectRatio="none" aria-hidden="true">
      <path d="M150 400 C 330 380, 560 330, 700 240 L700 400 Z" fill="var(--brand-blue)"/>
      <path d="M150 372 C 360 350, 560 300, 690 222" fill="none" stroke="var(--charcoal)" stroke-width="6"/>
      <path d="M150 386 C 360 364, 560 318, 700 236" fill="none" stroke="var(--white)" stroke-width="6"/>
    </svg>

    <div class="brand">
      <span class="brand__name">Keystone Audit</span>
      <span class="brand__tagline">Peer Review Specialists</span>
    </div>

    <div class="divider"></div>

    <div class="contact">
      <h1 class="contact__name">Marcus Dellow</h1>
      <p class="contact__role">Director / Structural Engineer</p>
      <p class="contact__creds">BEng(Hons), CPEng,<br>CMengNZ, IntPE(NZ)</p>
      <ul class="contact__list">
        <li>
          <svg viewBox="0 0 12 12"><path d="M2.5 1 L4.5 1 L5 3.5 L3.8 4.5 C4.5 6 6 7.5 7.5 8.2 L8.5 7 L11 7.5 L11 9.5 C11 10.5 10 11 9 11 C4.5 10.5 1.5 7.5 1 3 C1 2 1.5 1 2.5 1 Z" fill="var(--brand-blue)"/></svg>
          0219364058
        </li>
        <li>
          <svg viewBox="0 0 12 12"><rect x="1" y="2.5" width="10" height="7" fill="none" stroke="var(--brand-blue)" stroke-width="1.2"/><path d="M1 2.5 L6 6.5 L11 2.5" fill="none" stroke="var(--brand-blue)" stroke-width="1.2"/></svg>
          marcus.dellow@keystoneaudit.co.nz
        </li>
        <li>
          <svg viewBox="0 0 12 12"><circle cx="6" cy="6" r="5" fill="none" stroke="var(--brand-blue)" stroke-width="1.2"/><path d="M1 6 H11 M6 1 C3.5 4 3.5 8 6 11 M6 1 C8.5 4 8.5 8 6 11" fill="none" stroke="var(--brand-blue)" stroke-width="1"/></svg>
          www.keystoneaudit.co.nz
        </li>
      </ul>
    </div>
  </section>

</main>
</body>
</html>
```